Cannabis packaging label for a medicine bottle

This label will be for packaged cannabis. There are certain regulations that I will need incorporated such as warning symbols and mandatory wording on the label. The label will be for a medicine canister the measurements are 2 x 4.75. The primary photo will be in the center of the label. Please see photos attached of example label and also a photo of the container.

Product name: “Vela Pine”.....”Cannabis Flower”...”California Grown”

Target Market(s)

Young and older adults with a conservative sophisticated feel.

Font styles to use
Serif

Colors

Designer to choose colors to be used in the design.

Requirements
Must have
• Primary panel is the part of a cannabis product label that is most likely to be displayed, presented, shown, or examined under customary conditions of display for retail sale.
• Informational panel is any part of the cannabis product label that is not the primary panel and that contains required labeling information.
• All labels must be unobstructed and conspicuous, so the consumer can easily read the labels. The required information shall be located on the outside container or wrapper of the finished product and must have the following information, in no less that 6-point font.
• Primary Panel – All Products:
• Identity of product.
• Universal symbol (must be in black and white).
• Net weight 3.5 grams or volume of the contents in the package.
• Informational Panel – All Products:
• The applicable Government Warning.
• The CA Universal Symbol )may be no smaller than half (.5) inch by x half (.5) inch.)
• This is the applicable government warning for all flower products.
• Primary Panel – Manufactured Goods:
• The THC/CBD contents for the entire contents of the package in milligrams.
• Informational Panel – Manufactured Goods:
• Licensed manufacturer name and contact phone number or web address.
Nice to have
• Modern design but you and hip. Spray paint mame “Vela Pine”
Should not have
• Should not be appealing to children

```html
<!DOCTYPE html>
<html lang="en">
<head>
<meta charset="utf-8">
<title>Vela Pine – Cannabis Flower Labels</title>
<link rel="stylesheet" href="https://fonts.googleapis.com/css2?family=Bungee&family=Oswald:wght@400;500&family=Archivo+Narrow:wght@400;500&display=swap">
<style>
  :root{
    --bg:#f1f1f1;
    --label:#ffffff;
    --ink:#1d1d1d;
    --teal:#3aa8b2;
    --teal-light:#bfe3e8;
    --green:#6cb33f;
    --green-light:#d3e8b5;
    --lime:#a6d64a;
    --orange:#ee6a2a;
    --badge:#2f5fa6;
    --badge-gold:#d9b44a;
  }
  *{box-sizing:border-box;margin:0;padding:0}
  html,body{width:1200px;height:857px;overflow:hidden;background:var(--bg)}
  .canvas{position:relative;width:1200px;height:857px}
  .label{
    position:absolute;top:364px;width:196px;height:288px;
    background:var(--label);overflow:hidden;
    box-shadow:0 1px 3px rgba(0,0,0,.12);
  }
  .label--a{left:181px}.label--b{left:395px}.label--c{left:609px}.label--d{left:823px}

  /* primary panel */
  .artwork{position:absolute;inset:0}
  .artwork--vela{background:
    radial-gradient(circle at 30% 25%, #9ccf4a 0 18%, transparent 40%),
    radial-gradient(circle at 70% 55%, #2f9fb8 0 20%, transparent 45%),
    radial-gradient(circle at 40% 80%, #e0457a 0 12%, transparent 35%),
    linear-gradient(160deg,#c9d6d8,#7fb7c4 50%,#f0a540)}
  .artwork--flower{background:
    radial-gradient(circle at 45% 22%, #7dc245 0 18%, transparent 42%),
    radial-gradient(circle at 55% 45%, #f0672a 0 14%, transparent 36%),
    radial-gradient(circle at 40% 80%, #3bb07a 0 18%, transparent 42%),
    linear-gradient(160deg,#8a3a8c,#5e2c6e 55%,#3a6e4a)}
  .primary-name{
    position:absolute;left:0;right:0;top:28px;text-align:center;
    font-family:"Bungee",sans-serif;font-weight:400;line-height:1;white-space:nowrap;
  }
  .primary-name span{display:block}
  .label--a .primary-name span:first-child{font-size:50px;color:var(--lime)}
  .label--a .primary-name span:last-child{font-size:50px;color:#4fc3d0;margin-top:6px}
  .label--c .primary-name span:first-child{font-size:25px;color:var(--lime);margin-top:12px}
  .label--c .primary-name span:last-child{font-size:32px;color:var(--orange);margin-top:8px}
  .ca-symbol{position:absolute;width:42px;height:46px}
  .primary .ca-symbol{right:10px;top:178px}
  .net-weight{
    position:absolute;right:8px;bottom:20px;
    font:500 15px/1 "Oswald",sans-serif;color:var(--ink);
    background:rgba(255,255,255,.85);padding:3px 6px;transform:rotate(-6deg);
  }

  /* informational panel */
  .info .product-title{
    position:absolute;left:0;right:0;top:12px;
    font:400 21px/1 "Bungee",sans-serif;text-align:center;letter-spacing:-.5px;
    white-space:nowrap;
  }
  .label--b .product-title{color:var(--teal)}
  .label--d .product-title{color:var(--green);font-size:17px;top:14px}
  .warning{
    position:absolute;left:5px;right:5px;top:42px;
    font:400 6.2px/1.28 "Archivo Narrow",sans-serif;
    color:var(--ink);text-align:justify;
  }
  .facts{position:absolute;left:0;right:0;top:128px;height:100px}
  .info .ca-symbol{left:4px;top:4px}
  .potency{
    position:absolute;left:50px;top:4px;
    font:400 20px/1.2 "Oswald",sans-serif;color:var(--ink);letter-spacing:-.3px;
  }
  .badge{position:absolute;right:4px;top:6px;width:48px;height:48px}
  .use-note{
    position:absolute;left:0;right:0;top:66px;text-align:center;
    font:400 12px/1 "Oswald",sans-serif;color:var(--ink);
  }
  .address-band{
    position:absolute;left:0;right:0;top:242px;height:26px;
    font:400 14px/26px "Oswald",sans-serif;color:#fff;padding-left:6px;
  }
  .label--b .address-band{background:linear-gradient(90deg,var(--teal),var(--teal-light))}
  .label--d .address-band{background:linear-gradient(90deg,var(--green),var(--green-light))}
</style>
</head>
<body>
<main class="canvas">

  <!-- Vela Pine primary panel -->
  <section class="label label--a primary">
    <div class="artwork artwork--vela" role="img" aria-label="Colourful graffiti wall artwork with a spray can and street-art shapes"></div>
    <h2 class="primary-name"><span>VELA</span><span>PINE</span></h2>
    <svg class="ca-symbol" viewBox="0 0 42 46" aria-label="CA universal cannabis symbol">
      <polygon points="21,2 40,34 2,34" fill="#fff" stroke="#111" stroke-width="3"/>
      <rect x="19.5" y="13" width="3" height="11" fill="#111"/>
      <rect x="19.5" y="27" width="3" height="3" fill="#111"/>
      <text x="21" y="45" text-anchor="middle" font-family="Oswald, sans-serif" font-size="11" font-weight="500" fill="#111">CA</text>
    </svg>
    <div class="net-weight">NET WEIGHT 3.5 G</div>
  </section>

  <!-- Vela Pine informational panel -->
  <section class="label label--b info">
    <h2 class="product-title">VELA PINE</h2>
    <p class="warning">GOVERNMENT WARNING: THIS PRODUCT CONTAINS CANNABIS, A SCHEDULE I CONTROLLED SUBSTANCE. KEEP OUT OF REACH OF CHILDREN AND ANIMALS. CANNABIS PRODUCTS MAY ONLY BE POSSESSED OR CONSUMED BY PERSONS 21 YEARS OF AGE OR OLDER UNLESS THE PERSON IS A QUALIFIED PATIENT. THE INTOXICATING EFFECTS OF CANNABIS PRODUCTS MAY BE DELAYED UP TO TWO HOURS. CANNABIS USE WHILE PREGNANT OR BREASTFEEDING MAY BE HARMFUL. CONSUMPTION OF CANNABIS PRODUCTS IMPAIRS YOUR ABILITY TO DRIVE AND OPERATE MACHINERY. PLEASE USE EXTREME CAUTION.</p>
    <div class="facts">
      <svg class="ca-symbol" viewBox="0 0 42 46" aria-label="CA universal cannabis symbol">
        <polygon points="21,2 40,34 2,34" fill="#fff" stroke="#111" stroke-width="3"/>
        <rect x="19.5" y="13" width="3" height="11" fill="#111"/>
        <rect x="19.5" y="27" width="3" height="3" fill="#111"/>
        <text x="21" y="45" text-anchor="middle" font-family="Oswald, sans-serif" font-size="11" font-weight="500" fill="#111">CA</text>
      </svg>
      <p class="potency">THC: 150MG<br>CBD: 15MG</p>
      <svg class="badge" viewBox="0 0 58 58" role="img" aria-label="Quality seal">
        <circle cx="29" cy="29" r="27" fill="#fff" stroke="var(--badge)" stroke-width="4"/>
        <circle cx="29" cy="29" r="17" fill="none" stroke="var(--badge-gold)" stroke-width="3"/>
      </svg>
      <p class="use-note">For Medicinal Use Only</p>
    </div>
    <div class="address-band">ADDRESS:</div>
  </section>

  <!-- Cannabis Flower primary panel -->
  <section class="label label--c primary">
    <div class="artwork artwork--flower" role="img" aria-label="Purple graffiti wall artwork with street-art tags"></div>
    <h2 class="primary-name"><span>CANNABIS</span><span>FLOWER</span></h2>
    <svg class="ca-symbol" viewBox="0 0 42 46" aria-label="CA universal cannabis symbol">
      <polygon points="21,2 40,34 2,34" fill="#fff" stroke="#111" stroke-width="3"/>
      <rect x="19.5" y="13" width="3" height="11" fill="#111"/>
      <rect x="19.5" y="27" width="3" height="3" fill="#111"/>
      <text x="21" y="45" text-anchor="middle" font-family="Oswald, sans-serif" font-size="11" font-weight="500" fill="#111">CA</text>
    </svg>
    <div class="net-weight">NET WEIGHT 3.5 G</div>
  </section>

  <!-- Cannabis Flower informational panel -->
  <section class="label label--d info">
    <h2 class="product-title">CANNABIS FLOWER</h2>
    <p class="warning">GOVERNMENT WARNING: THIS PRODUCT CONTAINS CANNABIS, A SCHEDULE I CONTROLLED SUBSTANCE. KEEP OUT OF REACH OF CHILDREN AND ANIMALS. CANNABIS PRODUCTS MAY ONLY BE POSSESSED OR CONSUMED BY PERSONS 21 YEARS OF AGE OR OLDER UNLESS THE PERSON IS A QUALIFIED PATIENT. THE INTOXICATING EFFECTS OF CANNABIS PRODUCTS MAY BE DELAYED UP TO TWO HOURS. CANNABIS USE WHILE PREGNANT OR BREASTFEEDING MAY BE HARMFUL. CONSUMPTION OF CANNABIS PRODUCTS IMPAIRS YOUR ABILITY TO DRIVE AND OPERATE MACHINERY. PLEASE USE EXTREME CAUTION.</p>
    <div class="facts">
      <svg class="ca-symbol" viewBox="0 0 42 46" aria-label="CA universal cannabis symbol">
        <polygon points="21,2 40,34 2,34" fill="#fff" stroke="#111" stroke-width="3"/>
        <rect x="19.5" y="13" width="3" height="11" fill="#111"/>
        <rect x="19.5" y="27" width="3" height="3" fill="#111"/>
        <text x="21" y="45" text-anchor="middle" font-family="Oswald, sans-serif" font-size="11" font-weight="500" fill="#111">CA</text>
      </svg>
      <p class="potency">THC: 150MG<br>CBD: 15MG</p>
      <svg class="badge" viewBox="0 0 58 58" role="img" aria-label="Quality seal">
        <circle cx="29" cy="29" r="27" fill="#fff" stroke="var(--badge)" stroke-width="4"/>
        <circle cx="29" cy="29" r="17" fill="none" stroke="var(--badge-gold)" stroke-width="3"/>
      </svg>
      <p class="use-note">For Medicinal Use Only</p>
    </div>
    <div class="address-band">ADDRESS:</div>
  </section>

</main>
</body>
</html>
```